Tech Startup Needs Business Card Design

I am looking for an eye catching business card design for our new company, Torn Kite. We are a place for business owners and contractors to share their experiences with their customers and check their current customers. Our website, www.torn-kite.co, may be able to offer some guidance as to the design.

Industry/Entity Type

Business

Contact Information for Business Card

Owen Barthwick
888-417-3083
Owen@torn-kite.co
www.torn-kite.co

```html
<!DOCTYPE html>
<html lang="en">
<head>
<meta charset="utf-8">
<title>Torn Kite Business Card</title>
<link rel="stylesheet" href="https://fonts.googleapis.com/css2?family=Quicksand:wght@500;600&family=Signika:wght@700&display=swap">
<style>
  :root {
    --backdrop: #e4e6ea;
    --card-white: #ffffff;
    --card-black: #0b0c0d;
    --brand-red: #f50a0a;
    --fold-red: #a80000;
    --text-light: #ffffff;
  }
  * { box-sizing: border-box; margin: 0; padding: 0; }
  html, body { width: 1200px; height: 1200px; overflow: hidden; }
  body {
    background: var(--backdrop);
    font-family: "Quicksand", sans-serif;
    position: relative;
  }
  .card {
    position: absolute;
    left: 130px;
    width: 940px;
    height: 540px;
    overflow: hidden;
  }
  .card--front { top: 40px; background: var(--card-white); }
  .card--back { top: 620px; background: var(--card-black); }
  .card__shapes { position: absolute; inset: 0; width: 100%; height: 100%; }

  .brand {
    position: absolute;
    display: flex;
    align-items: center;
    gap: 18px;
    font-family: "Quicksand", sans-serif;
    font-weight: 600;
    font-size: 66px;
    letter-spacing: -1px;
    white-space: nowrap;
  }
  .brand__dot {
    width: 54px; height: 54px;
    border-radius: 50%;
    background: var(--brand-red);
    flex: none;
  }
  .brand--front { left: 60px; top: 225px; color: var(--brand-red); }
  .brand--back { left: 50%; top: 215px; transform: translateX(-50%); color: var(--text-light); }

  .holder-name {
    position: absolute;
    left: 482px;
    top: 203px;
    font-family: "Signika", sans-serif;
    font-weight: 700;
    font-size: 46px;
    color: var(--text-light);
    white-space: nowrap;
  }
  .contact-list {
    position: absolute;
    left: 537px;
    top: 345px;
    list-style: none;
  }
  .contact-list li {
    display: flex;
    align-items: center;
    gap: 14px;
    height: 46px;
    margin-bottom: 10px;
    color: var(--text-light);
    font-size: 20px;
    font-weight: 500;
  }
  .contact-icon { width: 44px; height: 44px; flex: none; }
</style>
</head>
<body>

<section class="card card--front" aria-label="Card front">
  <svg class="card__shapes" viewBox="0 0 940 540" aria-hidden="true">
    <polygon points="653,0 940,0 940,540 424,540" fill="var(--card-black)"/>
    <polygon points="0,490 215,490 285,540 0,540" fill="var(--brand-red)"/>
    <polygon points="455,270 540,270 511,335" fill="var(--fold-red)"/>
    <rect x="455" y="195" width="485" height="75" fill="var(--brand-red)"/>
  </svg>

  <div class="brand brand--front"><span class="brand__dot"></span>Torn Kite</div>

  <h1 class="holder-name">Owen Barthwick</h1>

  <ul class="contact-list">
    <li>
      <svg class="contact-icon" viewBox="0 0 44 44" aria-hidden="true">
        <circle cx="22" cy="22" r="22" fill="var(--brand-red)"/>
        <path d="M15 12c2-1 3 0 4 3s0 3-1 4c1 3 3 5 6 6 1-1 2-2 4-1s4 2 3 4-3 3-5 3c-7-1-13-7-14-14 0-2 1-4 3-5z" fill="#fff"/>
      </svg>
      888-417-3083
    </li>
    <li>
      <svg class="contact-icon" viewBox="0 0 44 44" aria-hidden="true">
        <circle cx="22" cy="22" r="22" fill="var(--brand-red)"/>
        <rect x="11" y="14" width="22" height="16" rx="1.5" fill="none" stroke="#fff" stroke-width="2.2"/>
        <polyline points="11,15 22,24 33,15" fill="none" stroke="#fff" stroke-width="2.2"/>
      </svg>
      Owen@torn-kite.co
    </li>
    <li>
      <svg class="contact-icon" viewBox="0 0 44 44" aria-hidden="true">
        <circle cx="22" cy="22" r="22" fill="var(--brand-red)"/>
        <g fill="none" stroke="#fff" stroke-width="2">
          <circle cx="22" cy="22" r="11"/>
          <ellipse cx="22" cy="22" rx="5" ry="11"/>
          <line x1="11" y1="22" x2="33" y2="22"/>
          <line x1="13" y1="16" x2="31" y2="16"/>
          <line x1="13" y1="28" x2="31" y2="28"/>
        </g>
      </svg>
      www.torn-kite.co
    </li>
  </ul>
</section>

<section class="card card--back" aria-label="Card back">
  <svg class="card__shapes" viewBox="0 0 940 540" aria-hidden="true">
    <rect x="0" y="152" width="137" height="231" fill="var(--brand-red)"/>
    <rect x="823" y="203" width="25" height="129" fill="var(--brand-red)"/>
    <rect x="855" y="203" width="85" height="129" fill="var(--brand-red)"/>
    <rect x="0" y="470" width="940" height="39" fill="var(--brand-red)"/>
  </svg>

  <div class="brand brand--back"><span class="brand__dot"></span>Torn Kite</div>
</section>

</body>
</html>
```